Harbour Thread Studio business card design

I need to get some business cards printed ready for company launch but my own designs look a bit basic and not very exciting, I hope you can help with something more eye catching.

I will be giving these to business owners, event organisers, brand managers etc. in a professional capacity with the aim that they keep me in mind and get in contact when they need to order embroidered/printed clothing items in future.
This is a basic website whilst new one is developed but the about us tab will give you better insight to the work i am looking for.

I also have facebook and instagram links on website so maybe if space for those icons?
also a business whatsapp account which there is a QR code for and something i may wish to include on the reverse so it's really easy for people to start a conversation.

Target Market(s)

Business to business

Industry/Entity Type

textile embroidery and printing

Contact Information for Business Card

name, job title, web address, email address

Font styles to use
Sans Serif
Other font styles liked:
• Monseratt is in the logo

Requirements
Must have
• name, job title, web address, email address, logo - nice design
Nice to have
• whatsapp qr link, social logos
Should not have
• no need for business address

```html
<!DOCTYPE html>
<html lang="en">
<head>
<meta charset="utf-8">
<title>Harbour Thread Studio – Business Card</title>
<link href="https://fonts.googleapis.com/css2?family=Montserrat:wght@500;600&display=swap" rel="stylesheet">
<style>
  :root {
    --stage: #000000;
    --card: #ffffff;
    --brand-blue: #6a77b0;
    --ring-grey: #808080;
    --muted: #7a7a7a;
    --icon-grey: #7d7d7d;
  }
  html, body {
    margin: 0;
    width: 1200px;
    height: 1000px;
    overflow: hidden;
    background: var(--stage);
    font-family: "Montserrat", Arial, sans-serif;
  }
  .canvas { position: relative; width: 1200px; height: 1000px; }
  .card {
    position: absolute;
    left: 260px;
    width: 680px;
    height: 389px;
    background: var(--card);
  }
  .card--front { top: 92px; }
  .card--back { top: 518px; }

  .brand-mark {
    position: absolute;
    border: 4px solid var(--ring-grey);
    border-radius: 50%;
    box-sizing: border-box;
    display: flex;
    align-items: center;
    justify-content: center;
    text-align: center;
  }
  .brand-name {
    color: var(--brand-blue);
    font-weight: 600;
    letter-spacing: 0.06em;
    line-height: 1.2;
    text-transform: uppercase;
  }
  .card--front .brand-mark { left: 238px; top: 50px; width: 168px; height: 168px; }
  .card--front .brand-name { font-size: 17px; }
  .card--back .brand-mark { left: 223px; top: 83px; width: 224px; height: 224px; }
  .card--back .brand-name { font-size: 22px; }

  .holder { position: absolute; left: 90px; top: 297px; }
  .holder-name {
    margin: 0;
    color: var(--brand-blue);
    font-size: 27px;
    font-weight: 500;
    line-height: 1;
    white-space: nowrap;
  }
  .holder-role {
    margin: 3px 0 0;
    color: var(--muted);
    font-size: 11px;
    font-weight: 500;
    white-space: nowrap;
  }
  .divider {
    position: absolute;
    left: 326px; top: 263px;
    width: 3px; height: 108px;
    background: var(--ring-grey);
  }
  .contact-list {
    position: absolute;
    left: 375px; top: 280px;
    margin: 0; padding: 0;
    list-style: none;
    color: var(--brand-blue);
    font-size: 17px;
    font-weight: 600;
    line-height: 22px;
    white-space: nowrap;
  }
  .contact-item { display: flex; align-items: flex-start; margin-bottom: 7px; }
  .contact-icon { width: 20px; height: 18px; margin: 2px 7px 0 0; flex: none; }
</style>
</head>
<body>
<div class="canvas">
  <section class="card card--front">
    <div class="brand-mark"><span class="brand-name">Harbour<br>Thread<br>Studio</span></div>

    <div class="holder">
      <p class="holder-name">Lena Marbach</p>
      <p class="holder-role">Norvik GmbH Geschäftsführerin</p>
    </div>

    <div class="divider"></div>

    <ul class="contact-list">
      <li class="contact-item">
        <svg class="contact-icon" viewBox="0 0 20 18" aria-hidden="true">
          <path d="M0 2h16l4 7-4 7H0z" fill="var(--icon-grey)"/>
          <path d="M4 6h9v6H4z M4 6l4.5 3.5L13 6" fill="none" stroke="#fff" stroke-width="1.3"/>
        </svg>
        lena.marbach@norvik.de
      </li>
      <li class="contact-item">
        <svg class="contact-icon" viewBox="0 0 20 18" aria-hidden="true">
          <path d="M0 2h16l4 7-4 7H0z" fill="var(--icon-grey)"/>
          <path d="M5 5c1-1 2-1 2.5 0l.8 1.6c.3.6 0 1-.5 1.3.6 1.3 1.4 2.1 2.7 2.7.3-.5.7-.8 1.3-.5l1.6.8c1 .5 1 1.5 0 2.5-3 1.5-9.5-5-8.4-8.4z" fill="#fff"/>
        </svg>
        +43 (0) 5120 / 38420 - 220
      </li>
      <li class="contact-item">
        <svg class="contact-icon" viewBox="0 0 20 18" aria-hidden="true">
          <path d="M0 1h16l4 8-4 8H0z" fill="var(--icon-grey)"/>
          <circle cx="8.5" cy="9" r="4.5" fill="none" stroke="#fff" stroke-width="1.2"/>
          <path d="M4 9h9 M8.5 4.5c-2 2.5-2 6.5 0 9 M8.5 4.5c2 2.5 2 6.5 0 9" fill="none" stroke="#fff" stroke-width="1"/>
        </svg>
        www.harbourthread.de
      </li>
    </ul>
  </section>

  <section class="card card--back">
    <div class="brand-mark"><span class="brand-name">Harbour<br>Thread<br>Studio</span></div>
  </section>
</div>
</body>
</html>
```